Maple Jubilee 2017 Poster

We need a poster design for our private school's annual Maple Jubilee. We're a progressive school in nyc, with deep community roots and a rich hundred year history. The community cherishes the events and looks forward to seeing what excitement each new year will bring! The posters will be displayed thoughout the school, appealing to a diverse audience of children and their' families.
We'd like a vintage vibe, circa turn of the 20th century (1900s). Please reference the images I've included, which give some inspiration. Also, as pertains to the theme, I'd like a representation of a vintage apple basket, brimming with apples, but with a planet earth nestled inside as the main focal point. Kind of like a words fair meets the harvest...
Also typography should be semi old fashioned looking as well.
COPY - Should Include the following:

Brook & Meadow
Maple Jubilee of Peoples

October 14th 12:00-4:00pm
Celebrate an Afternoon of Great Food, Music, Entertainment, & Fun

Tickets will be available for sale at Pickup

Target Market(s)

School Community, children and their parents, faculty, etc.

Industry/Entity Type

School

Font styles to use
Other font styles liked:
• Something old world fair, country looking

Colors
ec1f27
fcca95
ffcf3e

Requirements
Must have
• We'd like a vintage vibe, circa turn of the 20th century (1900s). Please reference the images I've included, which give some inspiration. Also, as pertains to the theme, I'd like a representation of a vintage apple basket, brimming with apples, but with a planet earth nestled inside as the main focal point. Kind of like a words fair meets the harvest...
• Also typography should be semi old fashioned looking as well.
• COPY - Should Include the following:
• Brook & Meadow
• Maple Jubilee of Peoples
• October 14th 12:00-4:00pm
• Celebrate an Afternoon of Great Food, Music, Entertainment, & Fun
• Tickets will be available for sale at Pickup
Nice to have
• Attractive design, draws you in, gets you interested in the event, informs you of important details.
Should not have
• I think that the design ask is pretty straight forward.

```html
<!DOCTYPE html>
<html lang="en">
<head>
<meta charset="utf-8">
<title>Maple Jubilee 2017 Poster</title>
<link rel="stylesheet" href="https://fonts.googleapis.com/css2?family=Limelight&family=Abril+Fatface&family=Playfair+Display:wght@400;700&display=swap">
<style>
  :root {
    --backdrop: #efefef;
    --wood-dark: #3d0608;
    --wood-mid: #5a0c0e;
    --festival-red: #ec1f27;
    --deep-red: #c8161c;
    --tablet-orange: #e0702e;
    --tablet-light: #ec8a3e;
    --peach: #fcca95;
    --gold: #ffcf3e;
    --gold-line: #e9b35a;
    --badge: #4a0709;
    --ribbon: #e88a2c;
    --ribbon-dark: #a8521a;
  }
  * { margin: 0; padding: 0; box-sizing: border-box; }
  html, body { width: 1200px; height: 848px; overflow: hidden; background: var(--backdrop); }
  .poster {
    position: absolute; left: 331px; top: 20px; width: 538px; height: 808px;
    background: linear-gradient(90deg, var(--wood-dark), var(--wood-mid) 30%, #4a090b 60%, var(--wood-dark));
    box-shadow: 0 2px 6px rgba(0,0,0,.35);
    overflow: hidden;
  }
  .poster__art { position: absolute; inset: 0; }
  .poster__text { position: absolute; left: 0; width: 100%; text-align: center; }
  .eyebrow {
    top: 146px; font-family: "Playfair Display", serif; font-size: 24px;
    letter-spacing: 3px; color: var(--peach); text-transform: uppercase; line-height: 1;
  }
  .headline { font-family: "Limelight", serif; color: var(--peach); line-height: 1; text-transform: uppercase; }
  .headline--main { top: 194px; font-size: 64px; letter-spacing: 2px; }
  .headline--second { top: 254px; font-size: 44px; letter-spacing: 3px; }
  .headline--third { top: 296px; font-size: 44px; letter-spacing: 1px; }
  .tickets-badge {
    position: absolute; left: 339px; top: 352px; width: 104px; height: 104px; border-radius: 50%;
    background: var(--badge); color: var(--peach);
    font-family: "Playfair Display", serif; font-size: 10.5px; line-height: 1.15;
    text-transform: uppercase; display: flex; align-items: center; justify-content: center; text-align: center;
  }
  .ribbon-copy {
    top: 562px; font-family: "Playfair Display", serif; font-weight: 700; font-size: 15px;
    line-height: 1.2; color: var(--peach); text-transform: uppercase; letter-spacing: .5px;
  }
  .event-date { top: 706px; font-family: "Abril Fatface", serif; font-size: 40px; color: var(--gold); line-height: 1; }
  .event-date__year { font-family: "Playfair Display", serif; font-weight: 400; }
  .event-time { top: 748px; font-family: "Playfair Display", serif; font-size: 17px; color: var(--gold); line-height: 1; }
</style>
</head>
<body>
<main class="poster">
  <svg class="poster__art" width="538" height="808" viewBox="0 0 538 808">
    <defs>
      <linearGradient id="tablet-fill" x1="0" y1="0" x2="0" y2="1">
        <stop offset="0" stop-color="var(--tablet-light)"/>
        <stop offset="1" stop-color="var(--tablet-orange)"/>
      </linearGradient>
    </defs>
    <g class="frame" stroke="var(--gold-line)" stroke-width="1.5" fill="none">
      <path d="M196 60 H31 V757 H196"/>
      <path d="M342 60 H508 V757 H342"/>
    </g>
    <rect class="ornament" role="img" aria-label="Gold calligraphic flourish" x="214" y="42" width="110" height="30" rx="12" fill="var(--gold-line)" opacity=".75"/>
    <path class="shield" d="M110 102 H418 Q453 102 453 140 V560 Q453 690 269 690 Q74 690 74 560 V140 Q74 102 110 102 Z" fill="var(--festival-red)"/>
    <path class="tablet" d="M118 124 H410 Q436 124 436 150 V489 H91 V150 Q91 124 118 124 Z" fill="url(#tablet-fill)"/>
    <path class="tablet-lower" d="M97 489 H431 V650 Q269 672 97 650 Z" fill="var(--deep-red)"/>
    <path class="basket-illustration" role="img" aria-label="Wooden apple basket brimming with red and yellow apples, with a globe of planet earth nestled inside" d="M210 420 Q210 382 260 382 H290 Q332 382 332 420 V462 H380 Q388 462 388 472 V630 Q388 648 370 648 H173 Q155 648 155 630 V472 Q155 462 165 462 H210 Z" fill="#d99a4c" opacity=".9"/>
    <path class="ribbon-tail" d="M19 612 L60 596 L50 622 L70 640 L28 642 Z" fill="var(--ribbon-dark)"/>
    <path class="ribbon-tail" d="M519 612 L478 596 L488 622 L468 640 L510 642 Z" fill="var(--ribbon-dark)"/>
    <path class="ribbon" d="M52 560 Q269 520 486 560 L486 616 Q269 576 52 616 Z" fill="var(--ribbon)"/>
  </svg>

  <p class="poster__text eyebrow">Brook &amp; Meadow</p>
  <h1 class="poster__text headline headline--main">Maple</h1>
  <p class="poster__text headline headline--second">Jubilee</p>
  <p class="poster__text headline headline--third">Of Peoples</p>
  <p class="tickets-badge">Tickets<br>will be<br>available<br>for sale at<br>drop off<br>and pick up</p>
  <p class="poster__text ribbon-copy">Celebrate with great food, music,<br>entertainment, and fun</p>
  <p class="poster__text event-date">October 14th <span class="event-date__year">2017</span></p>
  <p class="poster__text event-time">12:00-4:00PM</p>
</main>
</body>
</html>
```